Web Developer Needs a Business Card Design

I need a personal business card design that represents me as a web developer for potential employers. I would like the background to be a dark color on the front for contrast with my logo and name. The back will have all my information along with a smaller version of the logo. I want something with a modern look and feel, not too conservative. This will be used for potential employers and freelance work.

Industry/Entity Type

Business

Contact Information for Business Card

Front should have my logo and name. The back should have all my personal information which would include: name: Tom Brevardi, phone: 570-614-9083, email: tombrevardi@mailwisp.com, website url: www.tombrevardi.com, logo, web developer.

Font styles to use
Sans Serif

Requirements
Must have
• Must include my logo. The color palette base color will be the logo color.

```html
<!DOCTYPE html>
<html lang="en">
<head>
<meta charset="utf-8">
<title>Tom Brevardi – Business Card</title>
<link rel="stylesheet" href="https://fonts.googleapis.com/css2?family=Source+Sans+3:wght@400;600;700&display=swap">
<style>
  :root {
    --stage: #000000;
    --paper: #ffffff;
    --ink: #1b1b1b;
    --teal-soft: #66c7b4;
    --teal-bright: #52e5c5;
  }
  html, body {
    margin: 0;
    width: 1200px;
    height: 900px;
    overflow: hidden;
    background: var(--stage);
  }
  .card-sheet {
    display: block;
    width: 1200px;
    height: 900px;
    font-family: "Source Sans 3", "Myriad Pro", sans-serif;
  }
  .card-paper { fill: var(--paper); }
  .card-brand { fill: var(--teal-bright); }
  .mark-ring { fill: none; stroke: var(--teal-soft); stroke-width: 6; }
  .mark-name { fill: var(--teal-soft); font-weight: 600; font-size: 19px; }
  .holder-name { fill: var(--teal-soft); font-weight: 600; font-size: 18px; }
  .holder-role { fill: var(--ink); font-size: 13.5px; }
  .contact-line { fill: var(--ink); font-size: 13.5px; }
  .contact-icon { fill: var(--teal-soft); }
  .contact-icon-line { fill: none; stroke: var(--teal-soft); stroke-width: 1.6; stroke-linecap: round; }
  .hero-ring { fill: none; stroke: var(--paper); stroke-width: 14; }
  .hero-mark-name { fill: var(--paper); font-weight: 600; font-size: 46px; }
  .hero-name { fill: var(--paper); font-weight: 700; font-size: 21px; letter-spacing: 0.5px; }
</style>
</head>
<body>
<svg class="card-sheet" viewBox="0 0 1200 900" xmlns="http://www.w3.org/2000/svg">
  <defs>
    <clipPath id="brand-side-shape">
      <path d="M677 276 H1099 V513 A55 55 0 0 1 1044 568 H622 V331 A55 55 0 0 1 677 276 Z"/>
    </clipPath>
  </defs>

  <!-- Contact side -->
  <g class="contact-side">
    <path class="card-paper" d="M116 275 H538 A55 55 0 0 1 593 330 V568 H171 A55 55 0 0 1 116 513 Z"/>

    <g class="brand-mark">
      <circle class="mark-ring" cx="207" cy="362" r="60"/>
      <text class="mark-name" x="207" y="368" text-anchor="middle">Brevardi</text>
    </g>

    <text class="holder-name" x="575" y="440" text-anchor="end">Tom Brevardi</text>
    <text class="holder-role" x="575" y="458" text-anchor="end">Front-End Developer</text>

    <text class="contact-line" x="555" y="499" text-anchor="end">570-614-9083</text>
    <text class="contact-line" x="555" y="519" text-anchor="end">tombrevardi@mailwisp.com</text>
    <text class="contact-line" x="555" y="539" text-anchor="end">www.tombrevardi.com</text>

    <g class="phone-icon">
      <path class="contact-icon" d="M563 489 l2.5 -1 l2 3.5 l-1.5 1.2 q1 2.3 3 3.5 l1.3 -1.4 l3.4 2 l-0.9 2.5 q-5 0.4 -8.6 -4 q-2.6 -3.3 -1.2 -6.3 Z"/>
    </g>
    <g class="mail-icon">
      <rect class="contact-icon" x="563" y="510" width="10" height="7" rx="1"/>
      <path d="M563.5 510.5 L568 514 L572.5 510.5" fill="none" stroke="#ffffff" stroke-width="1"/>
    </g>
    <g class="link-icon">
      <path class="contact-icon-line" d="M566 536 l-1.5 1.5 a2 2 0 0 0 2.8 2.8 l1.5 -1.5 M569 533 l1.5 -1.5 a2 2 0 0 1 2.8 2.8 l-1.5 1.5 M566.5 537.5 l4 -4"/>
    </g>
  </g>

  <!-- Brand side -->
  <g class="brand-side">
    <path class="card-brand" d="M677 276 H1099 V513 A55 55 0 0 1 1044 568 H622 V331 A55 55 0 0 1 677 276 Z"/>
    <g clip-path="url(#brand-side-shape)">
      <circle class="hero-ring" cx="650" cy="420" r="204"/>
      <text class="hero-mark-name" x="636" y="436">Brevardi</text>
    </g>
    <text class="hero-name" x="885" y="514">TOM BREVARDI</text>
  </g>
</svg>
</body>
</html>
```